Verdant Loop Advisors, LLC

I am looking for a simple, clear layout with my logo prominent and embossed, on the best quality card stock available. I would like the business name and phone number included on the card as well......I dont want my name anywhere on the card and I would like my logo embossed on the card......something simple with a white back......open to designs as long as they go along with recycling symbols and green type stuff.....The address, website, cell number, fax number, and email are listed below

5374 Tillbury Fenwood Road
Larkmoor, MD 20799

c. 240.555.0143 f. 240.555.0187
e. sales@verdantloopadvisors.example
w. www.verdantloopadvisors.example

Industry/Entity Type

Recycling

```html
<!DOCTYPE html>
<html lang="en">
<head>
<meta charset="utf-8">
<title>Verdant Loop Advisors, LLC — Business Card</title>
<link rel="stylesheet" href="https://fonts.googleapis.com/css2?family=Open+Sans:wght@400;800&display=swap">
<style>
  :root {
    --backdrop: #8c9ba3;
    --card-green-light: #66d45f;
    --card-green: #47c041;
    --card-green-deep: #33a32f;
    --ink-brown: #3a281c;
    --ink-dark: #1b2417;
  }
  * { margin: 0; padding: 0; box-sizing: border-box; }
  html, body {
    width: 1200px;
    height: 960px;
    overflow: hidden;
    background: var(--backdrop);
  }
  .canvas {
    position: relative;
    width: 1200px;
    height: 960px;
    display: flex;
    align-items: center;
    justify-content: center;
  }
  .business-card {
    position: relative;
    width: 900px;
    height: 514px;
    background: linear-gradient(135deg, var(--card-green-light) 0%, var(--card-green) 55%, var(--card-green-deep) 100%);
    box-shadow: 0 18px 40px rgba(20, 30, 35, 0.35);
    font-family: "Open Sans", Arial, sans-serif;
  }
  .brand-square {
    position: absolute;
    left: 80px;
    top: 70px;
    width: 190px;
    height: 190px;
    background: var(--card-green-deep);
  }
  .brand-name {
    position: absolute;
    left: 330px;
    top: 62px;
    color: var(--ink-brown);
    font-weight: 800;
    font-size: 50px;
    line-height: 1.08;
    letter-spacing: 1px;
    text-transform: uppercase;
  }
  .contact-list {
    position: absolute;
    left: 336px;
    top: 250px;
    list-style: none;
    color: var(--ink-dark);
  }
  .contact-item {
    display: flex;
    align-items: center;
    gap: 16px;
    font-size: 24px;
    line-height: 1.2;
    margin-bottom: 12px;
  }
  .contact-item.address {
    align-items: flex-start;
    font-size: 20px;
  }
  .contact-address {
    font-style: normal;
  }
  .contact-icon {
    width: 24px;
    height: 24px;
    flex: none;
    fill: var(--ink-dark);
  }
</style>
</head>
<body>
<main class="canvas">
  <section class="business-card" aria-label="Verdant Loop Advisors business card">
    <div class="brand-square" aria-hidden="true"></div>
    <h1 class="brand-name">Verdant Loop<br>Advisors LLC</h1>

    <ul class="contact-list">
      <li class="contact-item">
        <svg class="contact-icon" viewBox="0 0 24 24" aria-label="Fax"><rect x="6" y="3" width="12" height="6"/><rect x="2" y="9" width="20" height="9" rx="2"/><rect x="6" y="15" width="12" height="6" fill="#66d45f" stroke="#1b2417" stroke-width="2"/></svg>
        <span>240.555.0187</span>
      </li>
      <li class="contact-item">
        <svg class="contact-icon" viewBox="0 0 24 24" aria-label="Phone"><path d="M6.6 10.8a15 15 0 0 0 6.6 6.6l2.2-2.2a1 1 0 0 1 1-.25 11.4 11.4 0 0 0 3.6.6 1 1 0 0 1 1 1V20a1 1 0 0 1-1 1A17 17 0 0 1 3 4a1 1 0 0 1 1-1h3.5a1 1 0 0 1 1 1c0 1.250.2 2.45.6 3.6a1 1 0 0 1-.25 1z"/></svg>
        <span>240.555.0143</span>
      </li>
      <li class="contact-item">
        <svg class="contact-icon" viewBox="0 0 24 24" aria-label="Email"><path d="M2 5h20v14H2z"/><path d="M2 5l10 8 10-8" fill="none" stroke="#66d45f" stroke-width="2"/></svg>
        <span>sales@verdantloopadvisors.example</span>
      </li>
      <li class="contact-item">
        <svg class="contact-icon" viewBox="0 0 24 24" aria-label="Website"><circle cx="12" cy="12" r="10" fill="none" stroke="#1b2417" stroke-width="2"/><ellipse cx="12" cy="12" rx="4" ry="10" fill="none" stroke="#1b2417" stroke-width="1.6"/><path d="M2 12h20M4 7h16M4 17h16" stroke="#1b2417" stroke-width="1.4"/></svg>
        <span>www.verdantloopadvisors.example</span>
      </li>
      <li class="contact-item address">
        <svg class="contact-icon" viewBox="0 0 24 24" aria-label="Address"><path d="M12 2a7 7 0 0 0-7 7c0 5 7 13 7 13s7-8 7-13a7 7 0 0 0-7-7zm0 9.5A2.5 2.5 0 1 1 12 6.5a2.5 2.5 0 0 1 0 5z"/></svg>
        <address class="contact-address">5374 Tillbury Fenwood Road<br>Larkmoor, MD 20799</address>
      </li>
    </ul>
  </section>
</main>
</body>
</html>
```